Business card for Property Management consultant

I need a business card for my business LX Vantage - I consult to real estate agents to improve the performance of their Property Management departments (rental houses management). The card needs to be very professional looking, incorporating our logo and my photo plus the line "Develop your Rent Roll to Perform"

Target Market(s)

Real Estate business owners

Industry/Entity Type

Business Consultant

Contact Information for Business Card

Business name - LX Vantage (logo uploaded)
My Name : Marcia Kellaway -
Title : Property Management Consultant

Develop your Rent Roll to perform

Phone : +61 438592716
email : marcia@lxvantage.com.au
website ; www.lxvantage.com.au

Requirements
Must have
• Logo
• My photo
• Very corporate / professional look

```html
<!DOCTYPE html>
<html lang="en">
<head>
<meta charset="utf-8">
<title>LX Vantage – Business Card</title>
<link href="https://fonts.googleapis.com/css2?family=Montserrat:wght@500;600&family=Source+Sans+3:wght@400;600;700&display=swap" rel="stylesheet">
<style>
  :root {
    --canvas: #eeeeec;
    --card-white: #ffffff;
    --brand-blue: #315ea9;
    --brand-blue-deep: #2a55a0;
    --link-blue: #2a4fa3;
    --gold: #c8922c;
    --ink: #1d1d1f;
    --on-blue: #ffffff;
    --faint-on-blue: rgba(255, 255, 255, 0.22);
  }
  * { margin: 0; padding: 0; box-sizing: border-box; }
  html, body {
    width: 1200px; height: 900px; overflow: hidden;
    background: var(--canvas);
    font-family: "Source Sans 3", sans-serif;
  }
  .stage { position: relative; width: 1200px; height: 900px; }

  .card {
    position: absolute;
    overflow: hidden;
    box-shadow: 0 6px 18px rgba(0, 0, 0, 0.18);
  }

  /* Front */
  .card-front {
    left: 78px; top: 35px; width: 588px; height: 363px;
    background: var(--card-white);
  }
  .card-front .bands { position: absolute; inset: 0; }
  .wordmark {
    position: absolute; left: 0; right: 0; top: 52px;
    text-align: center;
    font-family: "Montserrat", sans-serif;
    font-weight: 500; font-size: 52px; letter-spacing: 0.5px;
    color: var(--ink);
  }
  .strapline {
    position: absolute; left: 0; right: 0; top: 125px;
    text-align: center;
    font-family: "Montserrat", sans-serif;
    font-weight: 500; font-size: 16.5px; letter-spacing: 1.6px;
    color: var(--ink);
  }
  .promise {
    position: absolute; left: 0; right: 0; top: 162px;
    text-align: center;
    font-weight: 600; font-size: 17.5px;
    color: var(--link-blue);
  }
  .contact-list {
    position: absolute; left: 30px; top: 270px;
    list-style: none;
    color: var(--on-blue); font-size: 16.5px; line-height: 21px;
  }
  .contact-list li { display: flex; align-items: center; gap: 6px; }
  .contact-list svg { width: 11px; height: 11px; flex: none; }
  .person {
    position: absolute; right: 35px; top: 274px;
    text-align: right; color: var(--on-blue);
  }
  .person-name { font-weight: 700; font-size: 20.5px; line-height: 26px; }
  .person-title { font-size: 16.5px; line-height: 22px; }

  /* Back */
  .card-back {
    left: 388px; top: 505px; width: 567px; height: 352px;
    background: var(--brand-blue);
  }
  .portrait {
    position: absolute; left: 0; top: 0; width: 300px; height: 352px;
    background: radial-gradient(ellipse at 48% 45%, #c79a86 0%, #8a4a33 38%, rgba(42, 85, 160, 0.9) 72%, var(--brand-blue-deep) 100%);
  }
  .wordmark-faint {
    position: absolute; left: 250px; top: 50px;
    font-family: "Montserrat", sans-serif;
    font-weight: 500; font-size: 50px;
    color: var(--faint-on-blue);
  }
  .strapline-faint {
    position: absolute; left: 254px; top: 124px;
    font-family: "Montserrat", sans-serif;
    font-weight: 500; font-size: 15px; letter-spacing: 1.4px;
    color: var(--faint-on-blue);
  }
</style>
</head>
<body>
<main class="stage">

  <section class="card card-front" aria-label="Business card front">
    <svg class="bands" viewBox="0 0 588 363" aria-hidden="true">
      <polygon points="0,203 406,203 379,229 0,229" fill="var(--gold)"/>
      <polygon points="414,196 588,196 588,363 0,363 0,233 384,233" fill="var(--brand-blue)"/>
    </svg>

    <div class="wordmark">LX Vantage</div>
    <div class="strapline">STRATEGY - GROWTH - PROFIT</div>
    <div class="promise">Develop your Rent Roll to perform</div>

    <ul class="contact-list">
      <li>
        <svg viewBox="0 0 12 12"><path fill="#fff" d="M1 3.5C1 2 2.5 1 6 1s5 1 5 2.5L9.5 4.5 8 3.6V3H4v.6L2.5 4.5zM3 6l1.5-1.5h3L9 6v4.5H3z"/></svg>
        +61 438592716
      </li>
      <li>
        <svg viewBox="0 0 12 12"><rect x="1" y="2.5" width="10" height="7" fill="#fff"/><path d="M1 2.5l5 4 5-4" fill="none" stroke="var(--brand-blue)" stroke-width="1"/></svg>
        marcia@lxvantage.com.au
      </li>
      <li>
        <svg viewBox="0 0 12 12"><g fill="none" stroke="#fff" stroke-width="1.5"><rect x="1.5" y="5.5" width="5" height="3" rx="1.5" transform="rotate(-45 4 7)"/><rect x="5.5" y="3.5" width="5" height="3" rx="1.5" transform="rotate(-45 8 5)"/></g></svg>
        www.lxvantage.com.au
      </li>
    </ul>

    <div class="person">
      <div class="person-name">Marcia Kellaway</div>
      <div class="person-title">Property Management Consultant</div>
    </div>
  </section>

  <section class="card card-back" aria-label="Business card back">
    <div class="portrait" role="img" aria-label="Portrait photo of Marcia Kellaway in a blue blazer"></div>
    <div class="wordmark-faint">LX Vantage</div>
    <div class="strapline-faint">STRATEGY - GROWTH - PROFIT</div>
  </section>

</main>
</body>
</html>
```